Business card for Luxury Portable Restroom Trailer company

We are a Luxury Portable Restroom Trailer Company Called FALVEX HIRINGS. Based in Orange County California. We provide portable restroom trailers for events, such as, Weddings, Concerts, Charity events, Sporting events, Tournaments, Corporate events, ect. We rent and Sell the Luxury restrooms. Our colors are white, grey, and Orange. As you will see in the logo we uploaded.
There are 2 people in the company so the names and titles will change for the 3 people but card will remain the same. Here is the information for each Person: Desmond Purt CFO 555 018-3374
next Person: Milo Fenwright VP 555 018-3374
Next Person: Owen Fenwright CEO 555 018-3374
Information to include on the card: Luxury Restroom Trailers Rental and Sales. Weddings, Concerts, Charity, Sporting and Corp. Events.

```html
<!DOCTYPE html>
<html lang="en">
<head>
<meta charset="utf-8">
<title>Falvex Hirings — Business Card</title>
<link href="https://fonts.googleapis.com/css2?family=Montserrat:wght@400;500;700;800&display=swap" rel="stylesheet">
<style>
  :root {
    --orange: #ec6a27;
    --orange-deep: #e15a1f;
    --grey: #58585a;
    --white: #ffffff;
    --backdrop: #b9b9b9;
    --ink-light: #e9e9e9;
  }
  * { margin: 0; padding: 0; box-sizing: border-box; }
  html, body { width: 1200px; height: 802px; overflow: hidden; }
  body {
    background: linear-gradient(180deg, #cfcfcf 0%, var(--backdrop) 100%);
    font-family: "Montserrat", sans-serif;
    position: relative;
  }
  .card {
    position: absolute;
    top: 246px;
    width: 540px;
    height: 309px;
    border-radius: 18px;
    overflow: hidden;
    box-shadow: 0 14px 30px rgba(0,0,0,0.28);
  }
  .card--front { left: 45px; background: var(--white); }
  .card--back {
    left: 615px;
    background: linear-gradient(135deg, var(--orange) 0%, var(--orange-deep) 100%);
    display: flex; align-items: center; justify-content: center;
  }

  .front-bands { position: absolute; inset: 0; }

  .brand {
    position: absolute; left: 30px; top: 40px;
    display: flex; align-items: center; gap: 9px;
  }
  .brand__dot {
    width: 14px; height: 14px; border-radius: 50%;
    background: var(--orange);
  }
  .brand__name {
    font-weight: 800; font-size: 22px; letter-spacing: 1px;
    color: var(--orange); white-space: nowrap;
  }

  .person { position: absolute; left: 30px; top: 124px; color: var(--white); }
  .person__name {
    font-weight: 800; font-size: 20px; letter-spacing: 1px;
    color: var(--orange); text-transform: uppercase; white-space: nowrap;
  }
  .person__title { font-weight: 500; font-size: 12px; margin-top: 2px; color: var(--ink-light); }

  .contact { list-style: none; margin-top: 8px; }
  .contact li {
    display: flex; align-items: center; gap: 8px;
    font-size: 12.5px; font-weight: 500; color: var(--white);
    margin-bottom: 4px; white-space: nowrap;
  }
  .contact svg { width: 12px; height: 12px; flex: none; }

  .tagline { position: absolute; left: 30px; bottom: 18px; }
  .tagline__lead { font-size: 14px; font-weight: 500; color: var(--orange); white-space: nowrap; }
  .tagline__events { font-size: 13px; font-weight: 400; color: var(--grey); margin-top: 2px; white-space: nowrap; }

  .back-name {
    font-weight: 800; font-size: 44px; letter-spacing: 2px;
    color: var(--white); display: flex; align-items: center; gap: 14px;
    white-space: nowrap;
  }
  .back-name__dot { width: 22px; height: 22px; border-radius: 50%; background: var(--white); }
</style>
</head>
<body>

  <section class="card card--front" aria-label="Card front">
    <svg class="front-bands" viewBox="0 0 540 309" preserveAspectRatio="none">
      <polygon points="390,40 540,40 540,165 330,165" fill="var(--orange)"/>
      <polygon points="0,114 440,114 380,248 0,248" fill="var(--grey)"/>
      <circle cx="432" cy="124" r="62" fill="var(--white)"/>
      <circle cx="432" cy="124" r="53" fill="var(--orange)"/>
      <circle cx="432" cy="124" r="43" fill="var(--white)"/>
    </svg>

    <div class="brand">
      <span class="brand__dot"></span>
      <span class="brand__name">FALVEX HIRINGS</span>
    </div>

    <div class="person">
      <p class="person__name">Owen Fenwright</p>
      <p class="person__title">CEO</p>
      <ul class="contact">
        <li>
          <svg viewBox="0 0 16 16"><path fill="var(--orange)" d="M3.5 1.5l2.5 0 1.2 3.2-1.6 1.2a8 8 0 0 0 4.5 4.5l1.2-1.6 3.2 1.2v2.5a1.5 1.5 0 0 1-1.6 1.5A12.5 12.5 0 0 1 2 3.1 1.5 1.5 0 0 1 3.5 1.5z"/></svg>
          555 018-3374
        </li>
        <li>
          <svg viewBox="0 0 16 16"><rect x="1" y="3" width="14" height="10" rx="1.5" fill="var(--orange)"/><path d="M1.5 4l6.5 5 6.5-5" fill="none" stroke="var(--grey)" stroke-width="1.4"/></svg>
          owen@falvexhirings.com
        </li>
        <li>
          <svg viewBox="0 0 16 16"><circle cx="8" cy="8" r="7" fill="var(--orange)"/><path d="M1 8h14M8 1c-3 3.5-3 10.5 0 14M8 1c3 3.5 3 10.5 0 14" fill="none" stroke="var(--grey)" stroke-width="1.1"/></svg>
          www.falvexhirings.com
        </li>
      </ul>
    </div>

    <div class="tagline">
      <p class="tagline__lead">Luxury Restroom Trailers Rental and Sales</p>
      <p class="tagline__events">Weddings | Concerts | Charity | Sporting | Corp</p>
    </div>
  </section>

  <section class="card card--back" aria-label="Card back">
    <div class="back-name">
      <span class="back-name__dot"></span>
      <span>FALVEX HIRINGS</span>
    </div>
  </section>

</body>
</html>
```